Flyer Design removals

Tern Ridge Removals is a family run professional removal company specializing in all aspects of moving for private and business clients. We provide removals from small local moves to complete relocations and we strive to suit your circumstances and budget. Our aim is to offer efficient and effective removal service for reasonable prices. Our removals services are made straightforward and stress-free with our highly experienced team who handle your belongings with the utmost care and consideration.Our many years spent moving people and businesses provide us with the experience needed to make your move stress and hassle free. We can provide a wide range of packing, removal and storage services. Please fill in our quote request form on www.ternridgeremovals.co.uk as accurately as possible and one of our advisors will contact you with a firm quotation. Would you prefer to speak to us, please call today for the best value removal service you can get.
Industry/Entity Type
Business
Look and feel
Each slider illustrates characteristics of the customer's brand and the style your logo design should communicate.

```html
<!DOCTYPE html>
<html lang="en">
<head>
<meta charset="utf-8">
<title>Tern Ridge Removals flyers</title>
<link href="https://fonts.googleapis.com/css2?family=Open+Sans:wght@400;600;700&family=Roboto+Condensed:wght@400;700&display=swap" rel="stylesheet">
<style>
:root{
  --green:#6aaa3a;
  --green-dark:#4d8a26;
  --green-light:#8cc63f;
  --charcoal:#3a3a3c;
  --ink:#222;
  --white:#fff;
  --orange:#f7a81b;
  --bg:#e9e9e7;
}
*{box-sizing:border-box;margin:0;padding:0}
html,body{width:1200px;height:914px;overflow:hidden;background:var(--bg)}
body{position:relative;font-family:"Open Sans",sans-serif;color:var(--ink)}
.flyer{position:absolute;width:505px;height:712px;background:var(--white);box-shadow:0 4px 14px rgba(0,0,0,.25);overflow:hidden}
.flyer--services{left:64px;top:71px}
.flyer--quote{left:625px;top:135px}
.flyer__top{position:absolute;left:0;top:0;width:505px;height:345px;display:block}
.flyer__title{position:absolute;left:0;top:10px;width:100%;text-align:center;color:var(--white);font-weight:700;font-size:25px;letter-spacing:.2px}
.flyer__edge{position:absolute;top:300px;bottom:55px;width:5px;background:var(--green)}
.flyer__edge--l{left:0}.flyer__edge--r{right:0}
.brand{position:absolute;color:var(--green-dark);font-weight:700;font-size:30px;line-height:1.05}
.photo{position:absolute;border:1px solid #cfcfcf}
.intro{position:absolute;left:17px;top:444px;width:300px;font-size:10.2px;line-height:17px;text-align:justify}
.offer-bar{position:absolute;left:0;top:527px;width:313px;height:27px;background:linear-gradient(90deg,var(--green-dark),var(--green-light));color:var(--white);font-weight:700;font-size:16px;padding:3px 0 0 19px}
.offer-list{position:absolute;left:22px;top:566px;list-style:none;font-family:"Roboto Condensed",sans-serif;font-size:10.5px;text-transform:uppercase}
.offer-list li{display:flex;align-items:center;gap:6px;height:18.7px;white-space:nowrap}
.offer-list svg{width:13px;height:13px;flex:none}
.sticker{position:absolute;left:395px;top:565px;width:84px;height:84px;border-radius:50%;background:radial-gradient(circle at 40% 35%,#ffc43d,var(--orange));box-shadow:2px 3px 5px rgba(0,0,0,.25);display:flex;align-items:center;justify-content:center;text-align:center;color:var(--white);font-family:"Roboto Condensed",sans-serif;font-weight:700;font-size:10px;line-height:12px}
.call-bar{position:absolute;left:0;bottom:0;width:100%;height:57px;background:var(--charcoal);color:var(--white);display:flex;align-items:center;padding-left:18px;font-family:"Roboto Condensed",sans-serif;white-space:nowrap}
.call-bar__lead{font-size:15.5px;margin-right:12px}
.call-bar__lead strong{font-weight:700}
.call-bar__numbers{display:flex;align-items:center;gap:5px;font-size:17.5px;font-weight:700}
.call-bar__numbers svg{width:18px;height:18px;flex:none}
.call-bar__sep{font-weight:400;margin:0 3px}
.member-badge{position:absolute;left:259px;top:350px;width:200px;height:56px;border-radius:8px;background:#f1f1f1;border:1px solid #ddd}
.quote-heading{position:absolute;left:0;top:545px;width:100%;text-align:center;color:var(--green);font-weight:700;font-size:23px}
.quote-text{position:absolute;left:35px;top:578px;width:435px;text-align:center;font-size:11.3px;line-height:15px}
.quote-text a{color:var(--green);font-weight:700;text-decoration:none}
</style>
</head>
<body>

<section class="flyer flyer--services">
  <svg class="flyer__top" viewBox="0 0 505 345">
    <defs>
      <linearGradient id="homePhoto" x1="0" y1="0" x2="1" y2="1">
        <stop offset="0" stop-color="#f6f2ea"/><stop offset=".5" stop-color="#d9c9b0"/><stop offset="1" stop-color="#c9a77a"/>
      </linearGradient>
      <linearGradient id="band" x1="0" x2="1"><stop offset="0" stop-color="#8cc63f"/><stop offset="1" stop-color="#5c9e30"/></linearGradient>
    </defs>
    <g role="img" aria-label="Happy couple relaxing on a sofa among moving boxes in their new home">
      <rect x="0" y="30" width="505" height="290" fill="url(#homePhoto)"/>
    </g>
    <path d="M0 0H505V35Q250 80 0 45Z" fill="url(#band)"/>
    <path d="M0 45Q250 80 505 35V40Q250 85 0 50Z" fill="#fff"/>
    <path d="M0 272Q120 300 260 290T505 268V345H0Z" fill="url(#band)"/>
    <path d="M0 290Q130 325 270 305T505 300V345H0Z" fill="#fff"/>
  </svg>
  <h2 class="flyer__title">REMOVALS » PACKING » STORAGE</h2>
  <div class="flyer__edge flyer__edge--l"></div>

  <p class="brand" style="left:28px;top:340px;width:190px">Tern Ridge Removals</p>

  <p class="intro">Family run professional removal company specializing in all aspects of moving for private and business clients. We provide removals from small local moves to complete relocations and we strive to suit your circumstances and budget.</p>

  <div class="photo" role="img" aria-label="Removal van parked outside a white house" style="left:332px;top:351px;width:140px;height:94px;background:linear-gradient(#c9d3d8,#6f8a5a)"></div>
  <div class="photo" role="img" aria-label="Mover carrying a box down the van ramp" style="left:332px;top:459px;width:140px;height:94px;background:linear-gradient(#b9a384,#5f6f4c)"></div>

  <h3 class="offer-bar">WE OFFER</h3>
  <ul class="offer-list">
    <li><svg viewBox="0 0 13 13"><rect x="1" y="2" width="10" height="10" fill="none" stroke="#555"/><path d="M3 7l3 3 6-8" fill="none" stroke="#555" stroke-width="1.5"/></svg>Efficient and effective removal service for reasonable prices</li>
    <li><svg viewBox="0 0 13 13"><rect x="1" y="2" width="10" height="10" fill="none" stroke="#555"/><path d="M3 7l3 3 6-8" fill="none" stroke="#555" stroke-width="1.5"/></svg>Straightforward and stress-free</li>
    <li><svg viewBox="0 0 13 13"><rect x="1" y="2" width="10" height="10" fill="none" stroke="#555"/><path d="M3 7l3 3 6-8" fill="none" stroke="#555" stroke-width="1.5"/></svg>We handle your belongings with the utmost care and consideration</li>
    <li><svg viewBox="0 0 13 13"><rect x="1" y="2" width="10" height="10" fill="none" stroke="#555"/><path d="M3 7l3 3 6-8" fill="none" stroke="#555" stroke-width="1.5"/></svg>We provide a wide range of packing, removal and storage services</li>
  </ul>
  <div class="sticker">NO JOB IS<br>TOO BIG OR<br>TOO SMALL</div>

  <footer class="call-bar">
    <span class="call-bar__lead">Call today for your <strong>FREE QUOTE</strong></span>
    <span class="call-bar__numbers">
      <svg viewBox="0 0 20 20"><circle cx="10" cy="10" r="8.5" fill="none" stroke="#fff" stroke-width="1.5"/><path d="M7 5.5l2 2.5-1 1.2q1 2 3 3l1.2-1 2.5 2-1.2 1.5q-4 0-7.5-5Z" fill="#fff"/></svg>
      07700 900418<span class="call-bar__sep">|</span>0333 000 4127
    </span>
  </footer>
</section>

<section class="flyer flyer--quote">
  <svg class="flyer__top" viewBox="0 0 505 345">
    <defs>
      <linearGradient id="vanPhoto" x1="0" y1="0" x2="0" y2="1">
        <stop offset="0" stop-color="#b9d3ea"/><stop offset=".45" stop-color="#b67a5c"/><stop offset=".65" stop-color="#7f9a52"/><stop offset="1" stop-color="#5f8f32"/>
      </linearGradient>
      <linearGradient id="band2" x1="0" x2="1"><stop offset="0" stop-color="#8cc63f"/><stop offset="1" stop-color="#5c9e30"/></linearGradient>
    </defs>
    <g role="img" aria-label="Removal van parked on a lawn in front of a brick country house">
      <rect x="0" y="30" width="505" height="290" fill="url(#vanPhoto)"/>
    </g>
    <path d="M0 0H505V35Q250 80 0 45Z" fill="url(#band2)"/>
    <path d="M0 45Q250 80 505 35V40Q250 85 0 50Z" fill="#fff"/>
    <path d="M0 280Q120 300 260 292T505 278V345H0Z" fill="url(#band2)"/>
    <path d="M0 295Q130 325 270 310T505 305V345H0Z" fill="#fff"/>
  </svg>
  <h2 class="flyer__title">REMOVALS » PACKING » STORAGE</h2>
  <div class="flyer__edge flyer__edge--l"></div>
  <div class="flyer__edge flyer__edge--r"></div>

  <p class="brand" style="left:28px;top:345px;width:200px">Tern Ridge Removals</p>
  <div class="member-badge" aria-hidden="true"></div>

  <div class="photo" role="img" aria-label="Two removal vans parked on a drive" style="left:35px;top:441px;width:140px;height:94px;background:linear-gradient(#a7b0b8,#6a7560)"></div>
  <div class="photo" role="img" aria-label="Removal team carrying furniture outdoors" style="left:186px;top:441px;width:140px;height:94px;background:linear-gradient(#a8b89a,#52693a)"></div>
  <div class="photo" role="img" aria-label="Packer taping a cardboard box" style="left:337px;top:441px;width:140px;height:94px;background:linear-gradient(#dcd9d2,#b59a72)"></div>

  <h2 class="quote-heading">REMOVALS » PACKING » STORAGE</h2>
  <p class="quote-text">Please fill in our quote request form on <a href="#">www.ternridgeremovals.co.uk</a> as accurately as possible and one of our advisors will contact you with a firm quotation. Would you prefer to speak to us, please call today for the best value removal service you can get.</p>

  <footer class="call-bar">
    <span class="call-bar__lead">Call today for your <strong>FREE QUOTE</strong></span>
    <span class="call-bar__numbers">
      <svg viewBox="0 0 20 20"><circle cx="10" cy="10" r="8.5" fill="none" stroke="#fff" stroke-width="1.5"/><path d="M7 5.5l2 2.5-1 1.2q1 2 3 3l1.2-1 2.5 2-1.2 1.5q-4 0-7.5-5Z" fill="#fff"/></svg>
      07700 900418<span class="call-bar__sep">|</span>0333 000 4127
    </span>
  </footer>
</section>

</body>
</html>
```